Copper Lantern Stationery Design COMMITTED PAY

We need you to design stationary for a new Business called Copper Lantern. We have already got the logo designed and it is attached. Obviously we're looking for a stationery set designed around the colours and style to match the logo.

Use generic name, address, phone, fax, email etc ... I will edit text to required details.

What we need:
- Business Card Design Double Sided (90 x 55m + Bleed 3mm+)
- A4 Letter head Design
- A4 Presentation Folder Design
- Invoice Header Approx 210 x 55mm (Include Logo & Images)

And whatever other bonuses you'd like to kick in associated with the package.

I've attached some images and I've got hundreds more. If you want something else in the way of images, let me know.

I look forward to your seeing your designs.
Updates

Thought I should just clarify the follwoing:

1. The Invoice Header is just a branding for the top of my accounting package form.  It is not contain any contact information or the like.  Just logo, some images and some of your creativity and flair to bring it together.
2. The business does synthetic grass (75% of the business), Wetpour Rubber Surfaces, Softfall Surfaces and Rubber Wood Mulch.  These are categories you might choose to somehow highlight on the letterhead.
3. Business Card reverse side should be used to highlight the categories using images provided.

Wow, I've had some really nice designs submitted thus far, but my concern is that I can't just have an awesome looking card.  I really feel that my card needs to either show or say what we do.  Please make sure your design either shows or says the following:

- Synthetic Grass
- Wetpour Rubber Surfaces
- Softfall Surfaces
- Rubber Wood Mulch
- Shade Structures
- Landscape Structures

Just another note, don't know if I mentioned it or not in the original brief, but I prefer the use of icons instead of text for phone, email, fax etc labels.

Industry/Entity Type

Business

Requirements
Must have
• - Provide full editable source files
- Provide letterhead in MS Word format as well
- All designs must be awesome, but also show or say what we do. This is very important to me. I want anyone to look at our letterhead, business card etc and know instantly what it is that we do.
- Super quick turnaround on handover. I need card files to the printer on Monday morning (that's my Monday at GMT+10)
Nice to have
• - Creative use of the logo for a little bit of wow
Should not have
• - not square, boxy or rigid ... Loosen up a bit!

```html
<!DOCTYPE html>
<html lang="en">
<head>
<meta charset="utf-8">
<title>Copper Lantern – Business Card</title>
<link rel="stylesheet" href="https://fonts.googleapis.com/css2?family=Open+Sans:wght@400;600;700&display=swap">
<style>
  :root {
    --stage: #3a3a3a;
    --sky: #1e9be0;
    --sky-light: #4cc3f3;
    --sky-deep: #0b7fc8;
    --leaf: #6cbf2f;
    --ink: #2a2a2a;
    --rule: #b9b9b9;
    --paper: #ffffff;
  }
  * { box-sizing: border-box; margin: 0; padding: 0; }
  html, body { width: 1200px; height: 900px; overflow: hidden; }
  body {
    background: var(--stage);
    font-family: "Open Sans", Arial, sans-serif;
    position: relative;
  }
  .card {
    position: absolute;
    width: 560px;
    height: 342px;
    border-radius: 2px;
    overflow: hidden;
    box-shadow: 0 10px 30px rgba(0,0,0,.45);
  }

  /* Front */
  .card-front {
    left: 320px; top: 60px;
    background: radial-gradient(ellipse at 50% 50%, var(--sky-light) 0%, var(--sky) 45%, var(--sky-deep) 100%);
    display: flex; align-items: center; justify-content: center;
  }
  .front-brand { color: var(--paper); }
  .brand-row { display: flex; align-items: center; gap: 14px; }
  .brand-dot { flex: none; border-radius: 50%; border: 3px solid currentColor; }
  .brand-name {
    font-weight: 700; line-height: .95; text-transform: uppercase; letter-spacing: .5px;
  }
  .front-brand .brand-dot { width: 58px; height: 58px; }
  .front-brand .brand-name { font-size: 40px; }
  .front-brand .brand-tagline {
    margin: 8px 0 0 72px; font-size: 11px; font-weight: 600;
  }

  /* Back */
  .card-back {
    left: 280px; top: 470px;
    background: var(--paper);
    color: var(--ink);
  }
  .back-brand { position: absolute; left: 28px; top: 22px; }
  .back-brand .brand-row { gap: 10px; color: var(--sky); }
  .back-brand .brand-dot { width: 42px; height: 42px; border-color: var(--leaf); }
  .back-brand .brand-name { font-size: 28px; }
  .back-brand .brand-tagline { margin: 5px 0 0 52px; font-size: 9px; font-weight: 600; color: var(--sky); }

  .divider {
    position: absolute; left: 28px; right: 28px; top: 118px;
    height: 1px; background: var(--rule);
  }
  .address {
    position: absolute; left: 28px; top: 128px;
    font-size: 13px; line-height: 1.45; font-style: normal;
  }
  .contacts {
    position: absolute; left: 28px; top: 174px;
    display: grid; grid-template-columns: auto auto; column-gap: 22px; row-gap: 4px;
    font-size: 13px;
  }
  .contact { display: flex; align-items: center; gap: 7px; }
  .contact svg { width: 14px; height: 14px; flex: none; }

  .person { position: absolute; right: 30px; top: 234px; text-align: right; }
  .person-name { color: var(--leaf); font-weight: 700; font-size: 16px; }
  .person-role { font-size: 13px; }

  .band-leaf { position: absolute; left: 0; right: 0; bottom: 24px; height: 3px; background: var(--leaf); }
  .band-sky {
    position: absolute; left: 0; right: 0; bottom: 0; height: 20px;
    background: linear-gradient(90deg, var(--sky-deep), var(--sky-light) 50%, var(--sky-deep));
  }
</style>
</head>
<body>

<section class="card card-front" aria-label="Business card front">
  <div class="front-brand">
    <div class="brand-row">
      <span class="brand-dot"></span>
      <span class="brand-name">Copper<br>Lantern</span>
    </div>
    <p class="brand-tagline">Synthetic Grass &amp; Softfall Rubber Surfaces</p>
  </div>
</section>

<section class="card card-back" aria-label="Business card back">
  <div class="back-brand">
    <div class="brand-row">
      <span class="brand-dot"></span>
      <span class="brand-name">Copper<br>Lantern</span>
    </div>
    <p class="brand-tagline">Synthetic Grass &amp; Softfall Rubber Surfaces</p>
  </div>

  <div class="divider"></div>

  <address class="address">
    Harbour Lane 42-B7 5678 CD, Westbrook<br>
    PO Box 4471, 5678 CD, Westbrook
  </address>

  <div class="contacts">
    <div class="contact">
      <svg viewBox="0 0 16 16" aria-hidden="true"><path fill="var(--leaf)" d="M3 1.5l2.6-.4 1.3 3.4-1.7 1.2a8 8 0 0 0 5 5l1.2-1.7 3.4 1.3-.4 2.6c-.2.8-1 1.3-1.8 1.2C6.7 13.4 2.6 9.3 1.8 3.3 1.7 2.5 2.2 1.7 3 1.5z"/></svg>
      <span>555-014-2930</span>
    </div>
    <div class="contact">
      <svg viewBox="0 0 16 16" aria-hidden="true"><circle cx="8" cy="8" r="6.3" fill="none" stroke="var(--leaf)" stroke-width="1.8"/><circle cx="8" cy="8" r="2.2" fill="none" stroke="var(--leaf)" stroke-width="1.6"/></svg>
      <span>daniel@copperlantern.com</span>
    </div>
    <div class="contact">
      <svg viewBox="0 0 16 16" aria-hidden="true"><rect x="4" y="1.5" width="8" height="4" fill="none" stroke="var(--leaf)" stroke-width="1.5"/><rect x="1.5" y="5.5" width="13" height="6" rx="1" fill="var(--leaf)"/><rect x="4" y="10" width="8" height="4.5" fill="#fff" stroke="var(--leaf)" stroke-width="1.5"/></svg>
      <span>555-014-2939</span>
    </div>
    <div class="contact">
      <svg viewBox="0 0 16 16" aria-hidden="true"><circle cx="8" cy="8" r="6.3" fill="none" stroke="var(--leaf)" stroke-width="1.6"/><ellipse cx="8" cy="8" rx="2.8" ry="6.3" fill="none" stroke="var(--leaf)" stroke-width="1.3"/><path d="M1.8 8h12.4" stroke="var(--leaf)" stroke-width="1.3"/></svg>
      <span>www.copperlantern.com</span>
    </div>
  </div>

  <div class="person">
    <p class="person-name">Daniel Marsh</p>
    <p class="person-role">Director</p>
  </div>

  <div class="band-leaf"></div>
  <div class="band-sky"></div>
</section>

</body>
</html>
```